Orthopaedic Clinic Needs facebook page

Orthopaedic Clinic needs facebook page. The name of our clinic is Larchmont Orthopaedics. We focus on hip and knee orthopaedic conditions, as well as general orthopaedics. The main services are total knee replacements, total hip replacements, sports injury of the knee, hip fractures. Unique selling points of our service would be 1. Patient Centred Care, 2. Value Driven, 3. 2 Double-Fellowship Trained Surgeons.

Colour scheme should fit the logo design and be within the general colour recommendations of a medical clinic.

The design should be modern, eye catching, draws the end user to the website.

We would like to design our facebook page for future social media marketing.
In accordance with local advertisement regulations pertaining to medical clinics, no statements must have any information or laudatory statements such as the use of best, better, breakthrough, champions, or any statements that imply superiority and that may create unjustified expectations of services.

Target Market(s)

Patients
Friends family and relatives of patients.

Font styles to use
Serif
Sans Serif

Requirements
Must have
• My project must have my logo.

A nice colour scheme comfortable to the eye.
Nice to have
• Nice eye catching design that will draw the end user to the page.
Should not have
• Must not have any information that create unjustified expectaions.
Must not contain laudatory statements such as best, better, breakthrough, champions, or other statement that may create unjustified expecation of services.

```html
<!DOCTYPE html>
<html lang="en">
<head>
<meta charset="utf-8">
<title>Larchmont Orthopaedics – Cover</title>
<link rel="stylesheet" href="https://fonts.googleapis.com/css2?family=Michroma&display=swap">
<style>
  :root {
    --teal: #5db5b1;
    --teal-deep: #3f9d98;
    --slate: #5a636d;
    --ink: #2f3439;
    --name-grey: #5f6770;
    --paper: #ffffff;
    --stage: #e9eded;
  }
  * { margin: 0; padding: 0; box-sizing: border-box; }
  html, body { width: 1200px; height: 706px; overflow: hidden; background: var(--stage); }
  .canvas { position: relative; width: 1200px; height: 706px; }
  .cover {
    position: absolute; left: 0; top: 39px; width: 1200px; height: 628px;
    background: var(--paper); overflow: hidden;
    font-family: "Michroma", "Arial", sans-serif;
  }
  .hero-photo {
    position: absolute; left: 0; top: 0; width: 618px; height: 628px;
    background:
      radial-gradient(ellipse at 38% 45%, #f3f5f4 0%, #e4ecea 30%, rgba(228,236,234,0) 55%),
      linear-gradient(135deg, var(--teal) 0%, #8fcbc7 45%, #b7d6e6 75%, var(--teal-deep) 100%);
    border-radius: 0 0 48px 0;
  }
  .brand {
    position: absolute; right: 45px; top: 76px;
    display: flex; align-items: center; gap: 18px;
  }
  .brand-mark { width: 56px; height: 56px; background: var(--teal); border-radius: 6px; }
  .brand-name {
    color: var(--name-grey); font-size: 26px; line-height: 1.3; letter-spacing: 2px;
    text-align: left;
  }
  .services { position: absolute; left: 695px; top: 210px; width: 505px; list-style: none; }
  .service {
    position: relative; height: 50px; margin-bottom: 15px;
    clip-path: polygon(15px 0, 100% 0, 100% 100%, 15px 100%, 0 50%);
    color: var(--paper); font-size: 14px; letter-spacing: 0.5px;
    display: flex; align-items: center; justify-content: flex-end; padding-right: 45px;
  }
  .service--teal { background: var(--teal); }
  .service--slate { background: var(--slate); }
  .service::before {
    content: ""; position: absolute; left: 47px; top: 19px;
    width: 12px; height: 12px; border-radius: 50%; background: var(--paper);
  }
  .timeline {
    position: absolute; left: 752px; top: 235px; width: 1.5px; height: 195px;
    background: var(--paper); opacity: .85;
  }
  .contact { position: absolute; right: 59px; top: 502px; list-style: none; }
  .contact-item {
    display: flex; align-items: center; justify-content: flex-end; gap: 24px;
    height: 34px; margin-bottom: 15px; color: var(--ink); font-size: 13px;
  }
  .contact-icon {
    width: 33px; height: 33px; border-radius: 50%;
    display: flex; align-items: center; justify-content: center;
  }
  .contact-icon--teal { background: var(--teal); }
  .contact-icon--slate { background: var(--slate); }
</style>
</head>
<body>
<main class="canvas">
  <section class="cover">
    <div class="hero-photo" role="img" aria-label="Photo of a seated young woman holding her lower back in pain, framed by soft teal curved shapes"></div>

    <div class="brand">
      <span class="brand-mark"></span>
      <p class="brand-name">LARCHMONT<br>ORTHOPAEDICS</p>
    </div>

    <ul class="services">
      <li class="service service--teal">TOTAL KNEE REPLACEMENTS</li>
      <li class="service service--slate">TOTAL HIP REPLACEMENTS</li>
      <li class="service service--teal">SPORTS INJURY OF THE KNEE</li>
      <li class="service service--slate">HIP FRACTURES</li>
    </ul>
    <div class="timeline"></div>

    <ul class="contact">
      <li class="contact-item">
        <span>55-555-0142</span>
        <span class="contact-icon contact-icon--teal">
          <svg width="15" height="15" viewBox="0 0 24 24" aria-hidden="true">
            <path fill="#fff" d="M6.6 10.8a15.1 15.1 0 0 0 6.6 6.6l2.2-2.2a1 1 0 0 1 1-.25 11.4 11.4 0 0 0 3.6.57 1 1 0 0 1 1 1V20a1 1 0 0 1-1 1A17 17 0 0 1 3 4a1 1 0 0 1 1-1h3.5a1 1 0 0 1 1 1c0 1.25.2 2.45.57 3.57a1 1 0 0 1-.25 1z"/>
          </svg>
        </span>
      </li>
      <li class="contact-item">
        <span>HELLO@LARCHMONTORTHO.COM</span>
        <span class="contact-icon contact-icon--slate">
          <svg width="15" height="12" viewBox="0 0 20 15" aria-hidden="true">
            <rect x="1" y="1" width="18" height="13" rx="1" fill="none" stroke="#fff" stroke-width="1.6"/>
            <path d="M1.5 1.8 10 8.5l8.5-6.7M1.5 13.5l6-5.5M18.5 13.5l-6-5.5" fill="none" stroke="#fff" stroke-width="1.4"/>
          </svg>
        </span>
      </li>
    </ul>
  </section>
</main>
</body>
</html>
```